Postcard Front / Back For Computer Store with IT services

We are a computer store located in Hawaii on the island of Kauai. We would like to have a post card designed to market our services that we offer. We are a PC and Mac repair shop with full retail services.website: www.reefbyteshop.com the first thing that comes up is our service plan, we would like to market that, if you notice we have it Hawaii, meaning the background matches where we live etc, we would like to have the post card themed Hawaii.We offer a bunch of different Service contract Options for our customers:Signle computer 24.99/month Family Plan 29.99/month Business Plan 49.99/per computer month We also offer backup services much like vaultwisp but our own brand starting at 9.99/month.

website address https://www.reefbyteshop.com/online-backup/ for backup offerings..

Target Market(s)

Computer repair, IT services, Online backup, Remote Help Desk

Industry/Entity Type

Computer Repair

Requirements
Must have
• Should have front and Back color
• Phone number 808-519-3371
• website address www.reefbyteshop.com
Nice to have
• Plorin map with location on map
• Store hours mon - friday 9am - 6pm

```html
<!DOCTYPE html>
<html lang="en">
<head>
<meta charset="utf-8">
<title>ReefByte Postcard – Front and Back</title>
<link rel="stylesheet" href="https://fonts.googleapis.com/css2?family=Signika:wght@400;600;700&family=Oswald:wght@500&family=Ubuntu:wght@700&family=Tinos&display=swap">
<style>
  :root{
    --stage:#3b2a1f;
    --photo-dark:#2b2620;
    --photo-mid:#6b5a45;
    --photo-warm:#b98a6a;
    --panel:#f4f4f4;
    --ink:#262626;
    --blue:#1e8fd0;
    --blue-deep:#0f7fc2;
    --green:#6cbf2c;
    --green-soft:#8cc15a;
    --green-dark:#3f9a3a;
    --orange:#f26a21;
    --teal:#2a9e7c;
    --white:#ffffff;
  }
  *{margin:0;padding:0;box-sizing:border-box}
  html,body{width:750px;height:1200px;overflow:hidden;background:var(--stage)}
  .canvas{position:relative;width:750px;height:1200px}

  /* ---------- Front ---------- */
  .card-front{position:absolute;left:0;top:32px;width:750px;height:570px;overflow:hidden}
  .front-photo{position:absolute;inset:0;
    background:linear-gradient(120deg,var(--photo-dark) 0%,var(--photo-mid) 40%,var(--photo-warm) 70%,var(--photo-dark) 100%)}
  .header-accent{position:absolute;left:0;top:38px;width:620px;height:90px;background:var(--blue)}
  .header{position:absolute;left:0;top:28px;width:608px;height:96px;background:var(--panel)}
  .brand{position:absolute;left:32px;top:30px;display:flex;align-items:center;gap:10px;
    font-family:"Signika",sans-serif;font-weight:700;font-size:34px;color:var(--blue)}
  .brand-mark{width:22px;height:22px;background:var(--green)}
  .site-name{position:absolute;left:366px;top:16px;font-family:"Tinos",serif;font-size:32px;line-height:36px;color:var(--teal)}
  .site-name .dot{color:var(--blue)}
  .site-name .tld{color:#333}
  .hours{position:absolute;left:340px;top:60px;display:flex;align-items:center;gap:6px;white-space:nowrap;
    font-family:"Ubuntu",sans-serif;font-weight:700;font-size:12px;color:var(--ink)}
  .hours em{font-style:normal;color:var(--blue)}

  .plan-panel{position:absolute;left:0;top:216px;width:456px;height:238px;background:rgba(244,244,244,.95)}
  .plan-tab{position:absolute;left:0;top:202px;width:246px;height:38px;background:var(--blue);
    clip-path:polygon(0 0,100% 0,92% 100%,0 100%)}
  .plan-title{position:absolute;left:35px;top:205px;font-family:"Oswald",sans-serif;font-weight:500;font-size:23px;color:var(--ink);letter-spacing:.5px}
  .plan-title span{color:var(--orange)}
  .features{position:absolute;list-style:none;font-family:"Signika",sans-serif;font-size:11px;line-height:15px;color:var(--ink)}
  .features li{position:absolute;padding-left:23px}
  .features li svg{position:absolute;left:0;top:0}
  .features.left{left:36px;top:256px;width:190px}
  .features.right{left:240px;top:254px;width:205px}

  .price-badge{position:absolute;left:540px;top:300px}

  .contact-label{position:absolute;left:27px;top:490px;font-family:"Ubuntu",sans-serif;font-weight:700;font-size:15px;color:var(--white)}
  .contact-bar{position:absolute;left:0;top:523px;width:750px;height:47px;background:var(--blue-deep)}
  .contact-bar .green{position:absolute;left:0;top:0;width:390px;height:47px;background:var(--green-soft);border-radius:0 24px 24px 0}
  .contact-item{position:absolute;display:flex;align-items:center;gap:10px;white-space:nowrap;font-family:"Tinos",serif;color:var(--white)}
  .web{left:30px;top:11px;font-size:14px}
  .phone{left:222px;top:10px;font-size:18px}
  .address{position:absolute;top:8px;font-family:"Tinos",serif;font-size:11px;line-height:15px;color:var(--white);white-space:nowrap}

  /* ---------- Back ---------- */
  .card-back{position:absolute;left:0;top:612px;width:750px;height:564px;overflow:hidden;background:var(--blue)}
  .back-photo{position:absolute;left:0;top:0;width:410px;height:564px;
    background:linear-gradient(150deg,var(--photo-mid) 0%,var(--photo-dark) 45%,var(--photo-mid) 80%)}
  .back-shape{position:absolute;left:0;top:0}
  .stamp-box{position:absolute;left:620px;top:46px;width:82px;height:86px;border:3px solid var(--white)}
  .vertical-site{position:absolute;left:350px;top:312px;transform:rotate(-90deg);transform-origin:left top;
    font-family:"Tinos",serif;font-size:28px;color:var(--green-dark);white-space:nowrap}
  .vertical-site .dot{color:var(--blue)}
  .back-brand{position:absolute;left:95px;top:470px;display:flex;align-items:center;gap:10px;
    font-family:"Signika",sans-serif;font-weight:700;font-size:34px;color:var(--blue)}
</style>
</head>
<body>
<main class="canvas">

  <section class="card-front">
    <div class="front-photo" role="img" aria-label="Close-up photo of hands fitting a memory module into a computer motherboard"></div>

    <div class="header-accent"></div>
    <header class="header">
      <div class="brand"><span class="brand-mark"></span>ReefByte</div>
      <div class="site-name">reefbyteshop<span class="dot">.</span><span class="tld">com</span></div>
      <div class="hours">
        <svg width="22" height="22" viewBox="0 0 22 22"><circle cx="11" cy="11" r="9.5" fill="none" stroke="#262626" stroke-width="2"/><path d="M11 5v6l-3 3" fill="none" stroke="#262626" stroke-width="2"/></svg>
        <span>Store hours mon - friday <em>9am - 6pm</em></span>
      </div>
    </header>

    <div class="plan-panel"></div>
    <div class="plan-tab"></div>
    <h2 class="plan-title">SERVICE <span>PLAN</span></h2>

    <ul class="features left">
      <li style="top:0"><svg width="17" height="17" viewBox="0 0 17 17"><circle cx="8.5" cy="8.5" r="8.5" fill="#6cbf2c"/><path d="M4.5 8.8l2.7 2.6 5-5" fill="none" stroke="#fff" stroke-width="2"/></svg>Unlimited Virus Removals Only applies to PCs and laptops.($139.99 Value)</li>
      <li style="top:53px"><svg width="17" height="17" viewBox="0 0 17 17"><circle cx="8.5" cy="8.5" r="8.5" fill="#6cbf2c"/><path d="M4.5 8.8l2.7 2.6 5-5" fill="none" stroke="#fff" stroke-width="2"/></svg>Unlimited Computer Tune-ups ($84.99 Value)</li>
      <li style="top:91px"><svg width="17" height="17" viewBox="0 0 17 17"><circle cx="8.5" cy="8.5" r="8.5" fill="#6cbf2c"/><path d="M4.5 8.8l2.7 2.6 5-5" fill="none" stroke="#fff" stroke-width="2"/></svg>Kauai Based Company</li>
      <li style="top:125px"><svg width="17" height="17" viewBox="0 0 17 17"><circle cx="8.5" cy="8.5" r="8.5" fill="#6cbf2c"/><path d="M4.5 8.8l2.7 2.6 5-5" fill="none" stroke="#fff" stroke-width="2"/></svg>Unlimited Device Setups Get your camera, MP3 player or printer setup.</li>
    </ul>
    <ul class="features right">
      <li style="top:0"><svg width="17" height="17" viewBox="0 0 17 17"><circle cx="8.5" cy="8.5" r="8.5" fill="#6cbf2c"/><path d="M4.5 8.8l2.7 2.6 5-5" fill="none" stroke="#fff" stroke-width="2"/></svg>Includes Internet Security Software ($299.99 value)</li>
      <li style="top:38px"><svg width="17" height="17" viewBox="0 0 17 17"><circle cx="8.5" cy="8.5" r="8.5" fill="#6cbf2c"/><path d="M4.5 8.8l2.7 2.6 5-5" fill="none" stroke="#fff" stroke-width="2"/></svg>Unlimited Troubleshooting On printers, email and software.</li>
      <li style="top:79px"><svg width="17" height="17" viewBox="0 0 17 17"><circle cx="8.5" cy="8.5" r="8.5" fill="#6cbf2c"/><path d="M4.5 8.8l2.7 2.6 5-5" fill="none" stroke="#fff" stroke-width="2"/></svg>Filtered DNS Service ($49.99/month Value)</li>
      <li style="top:118px"><svg width="17" height="17" viewBox="0 0 17 17"><circle cx="8.5" cy="8.5" r="8.5" fill="#6cbf2c"/><path d="M4.5 8.8l2.7 2.6 5-5" fill="none" stroke="#fff" stroke-width="2"/></svg>Unlimited Remote Support ($84.99 Value)</li>
      <li style="top:156px"><svg width="17" height="17" viewBox="0 0 17 17"><circle cx="8.5" cy="8.5" r="8.5" fill="#6cbf2c"/><path d="M4.5 8.8l2.7 2.6 5-5" fill="none" stroke="#fff" stroke-width="2"/></svg>Free Online/Local Backup Software($99.99 Value)</li>
    </ul>

    <svg class="price-badge" width="120" height="130" viewBox="0 0 120 130" aria-label="Start at $24.99 per month, free setup">
      <path d="M48 100h24v20l-12-6-12 6z" fill="#f26a21"/>
      <polygon points="60,6 106,32 106,84 60,110 14,84 14,32" fill="#2a2a2a" stroke="#555" stroke-width="3"/>
      <polygon points="60,16 97,37 97,79 60,100 23,79 23,37" fill="none" stroke="#bbb" stroke-width="1" stroke-dasharray="3 3"/>
      <polygon points="60,0 72,6 72,22 60,28 48,22 48,6" fill="#f26a21"/>
      <text x="60" y="14" text-anchor="middle" font-family="Signika,sans-serif" font-size="7" fill="#fff">Start</text>
      <text x="60" y="22" text-anchor="middle" font-family="Signika,sans-serif" font-size="7" fill="#fff">at</text>
      <text x="60" y="63" text-anchor="middle" font-family="Signika,sans-serif" font-weight="700" fill="#fff"><tspan font-size="10">$</tspan><tspan font-size="22">24.99</tspan><tspan font-size="9">/MO</tspan></text>
      <text x="60" y="80" text-anchor="middle" font-family="Signika,sans-serif" font-size="10" fill="#fff">FREE Setup</text>
    </svg>

    <h3 class="contact-label">Contact Us</h3>
    <footer class="contact-bar">
      <div class="green"></div>
      <div class="contact-item web">
        <svg width="24" height="24" viewBox="0 0 24 24" fill="none" stroke="#fff" stroke-width="1.6"><circle cx="12" cy="12" r="10.5"/><ellipse cx="12" cy="12" rx="4.5" ry="10.5"/><path d="M1.5 12h21M3.5 6.5h17M3.5 17.5h17"/></svg>
        www.reefbyteshop.com
      </div>
      <div class="contact-item phone">
        <svg width="22" height="22" viewBox="0 0 24 24"><path d="M6.6 10.8a15 15 0 0 0 6.6 6.6l2.2-2.2a1 1 0 0 1 1-.25 11 11 0 0 0 3.6.6 1 1 0 0 1 1 1V20a1 1 0 0 1-1 1A17 17 0 0 1 3 4a1 1 0 0 1 1-1h3.5a1 1 0 0 1 1 1 11 11 0 0 0 .6 3.6 1 1 0 0 1-.25 1z" fill="#fff"/></svg>
        808-519-3371
      </div>
      <svg style="position:absolute;left:432px;top:8px" width="18" height="28" viewBox="0 0 18 28"><path d="M9 1a8 8 0 0 0-8 8c0 6 8 17 8 17s8-11 8-17a8 8 0 0 0-8-8z" fill="none" stroke="#fff" stroke-width="2"/><circle cx="9" cy="9" r="3" fill="#fff"/></svg>
      <p class="address" style="left:461px">REEFBYTE LLC.<br>4411 Niu Street</p>
      <p class="address" style="left:590px">Suite 207<br>Koholua, Hawaii 96788</p>
    </footer>
  </section>

  <section class="card-back">
    <div class="back-photo" role="img" aria-label="Photo of a hand installing a component beside a CPU cooler fan on a motherboard"></div>
    <svg class="back-shape" width="750" height="564" viewBox="0 0 750 564">
      <polygon points="420,0 750,0 750,120 420,260" fill="#2a9ad8" opacity=".35"/>
      <polygon points="420,330 750,240 750,300 420,380" fill="#ffffff" opacity=".06"/>
      <path d="M410 0H352Q322 0 322 40L322 120C322 260 290 330 190 400C110 455 30 480 0 530V564H410Z" fill="var(--green)"/>
      <path d="M402 0H362Q334 0 334 40L334 120C334 262 304 336 204 406C124 461 40 490 0 550V564H402Z" fill="#fff"/>
      <rect x="402" y="0" width="7" height="564" fill="var(--green)"/>
    </svg>
    <div class="stamp-box"></div>
    <div class="vertical-site">reefbyteshop<span class="dot">.</span>com</div>
    <div class="back-brand"><span class="brand-mark"></span>ReefByte</div>
  </section>

</main>
</body>
</html>
```